Grand Opening Banner needed for Marvelous Floors and Home

My website is www.MarvelousFloorsandHome.example (login with password 'plorvak')

A full page banner 1000px X 500px with bright, lively colors and wording that shows an exciting GRAND OPENING celebration throughout the site. Banner needs to convey the following...

Grand Opening Sale
Runs through end of the month
Savings in every department
30 day Returns
Free Rug Pads with every rug
Free shipping.

Banner can be a simple background with graphics and text, or can be a room scene with rugs and furniture, or a grouping of rugs with text.

Some Ideas and Images can be taken from our vendor's websites, such as:

http://tvsupplyhub.example/
http://borvane.example/borvane_2015/
http://www.pxweaves.example/
http://tassiru.example/
http://shopvelmira.example/

I also have quite a few room scene images available for use, if you desire.

Target Market(s)

Affluent women who care about stylish decor for their homes

Industry/Entity Type

Home And Garden

Requirements
Must have
• bold, vibrant appearance. Text that can be modified in Photoshop.
Nice to have
• HAND DRAWN, ARTIST STYLE ARTWORK IS GREATLY APPRECIATED.
• flat graphics and text with little to no 3 dimensional (shadow) effect. Font styles should be elegant/luxurious. An organic, scribbled, or painted style is nice in keeping with the handmade products that we sell.
• I am open to changing the color scheme of the website, to match your banner, so don't feel tied down to my existing colors.
Should not have
• nothing too modern or extreme in style.

```html
<!DOCTYPE html>
<html lang="en">
<head>
<meta charset="utf-8">
<title>Grand Opening Sale Banner</title>
<link rel="stylesheet" href="https://fonts.googleapis.com/css2?family=Great+Vibes&family=Montserrat:wght@700&family=Tinos:wght@400;700&display=swap">
<style>
  :root {
    --scene-light: #e9e2d6;
    --scene-mid: #b9a68d;
    --scene-dark: #5a2a1c;
    --circle-tan: #bfb08f;
    --diamond-taupe: #8f8a70;
    --diamond-brown: #5d4b3b;
    --diamond-mauve: #8d8589;
    --diamond-ochre: #bf8e48;
    --diamond-olive: #9c9a5c;
    --text-light: #ffffff;
  }
  html, body {
    margin: 0;
    padding: 0;
    width: 1200px;
    height: 600px;
    overflow: hidden;
    background: #ffffff;
  }
  .banner {
    position: relative;
    width: 1200px;
    height: 600px;
    overflow: hidden;
  }
  .room-scene {
    position: absolute;
    inset: 0;
    background:
      linear-gradient(180deg, rgba(255,255,255,0) 55%, rgba(90,42,28,0.55) 100%),
      linear-gradient(90deg, var(--scene-light) 0%, #d8cfc0 30%, var(--scene-mid) 62%, #8a6f55 100%);
  }
  .offer-art {
    position: absolute;
    inset: 0;
    width: 1200px;
    height: 600px;
  }
  .headline-script {
    font-family: "Great Vibes", cursive;
    font-size: 68px;
    fill: var(--text-light);
  }
  .headline-sale {
    font-family: "Montserrat", sans-serif;
    font-weight: 700;
    font-size: 64px;
    letter-spacing: 1px;
    fill: var(--text-light);
  }
  .offer-text {
    font-family: "Tinos", serif;
    font-size: 22px;
    fill: var(--text-light);
    text-anchor: middle;
  }
  .offer-text .strong { font-weight: 700; }
</style>
</head>
<body>
<main class="banner">
  <div class="room-scene" role="img" aria-label="Photo of a bright living room: two children with headphones lying on a patterned area rug, a sofa, lamp, coffee table and a geometric rug on a dark wood floor"></div>

  <svg class="offer-art" viewBox="0 0 1000 500" xmlns="http://www.w3.org/2000/svg">
    <circle class="headline-circle" cx="512" cy="128" r="230" fill="var(--circle-tan)"/>

    <text class="headline-script" x="515" y="92" text-anchor="middle">Grand Opening</text>
    <text class="headline-sale" x="513" y="174" text-anchor="middle">SALE</text>

    <polygon class="diamond-end-of-month" points="370,155 490,272 370,389 250,272" fill="var(--diamond-taupe)"/>
    <polygon class="diamond-returns" points="665,145 792,262 665,379 538,262" fill="var(--diamond-mauve)"/>
    <polygon class="diamond-departments" points="515,212 635,332 515,452 395,332" fill="var(--diamond-brown)"/>
    <polygon class="diamond-rug-pads" points="393,312 498,414 393,516 288,414" fill="var(--diamond-ochre)"/>
    <polygon class="diamond-shipping" points="662,282 780,392 662,502 544,392" fill="var(--diamond-olive)"/>

    <text class="offer-text">
      <tspan x="357" y="226">RUNS</tspan>
      <tspan x="357" y="249">THROUGH</tspan>
      <tspan x="357" y="272">END OF THE</tspan>
      <tspan x="357" y="295">MONTH</tspan>
    </text>
    <text class="offer-text">
      <tspan x="668" y="218">30</tspan>
      <tspan x="668" y="240">DAY</tspan>
      <tspan x="668" y="262">RETURNS</tspan>
    </text>
    <text class="offer-text">
      <tspan x="515" y="291">SAVINGS</tspan>
      <tspan x="515" y="313">IN EVERY</tspan>
      <tspan x="515" y="335">DEPARTMENT</tspan>
    </text>
    <text class="offer-text">
      <tspan class="strong" x="393" y="374">FREE</tspan>
      <tspan x="393" y="397">RUG PADS</tspan>
      <tspan x="393" y="419">WITH</tspan>
      <tspan x="393" y="441">EVERY RUG</tspan>
    </text>
    <text class="offer-text">
      <tspan class="strong" x="663" y="378">FREE</tspan>
      <tspan x="663" y="401">SHIPPING</tspan>
    </text>
  </svg>
</main>
</body>
</html>
```